Suspended swing stage rental

We rent suspended swing stages, rigging soultions set up, teardown and operate.

Change the verbage around
When your crew requires versatile exterior access to a high-rise building, Crestwick Rentals Scaffolding Services can provide you with the suspended scaffolding rental you need to focus on the job at hand. Our experts create swing stage packages for access to buildings and other structures with various shapes, contours, and complex angles for use in a variety of commercial applications.

```html
<!DOCTYPE html>
<html lang="en">
<head>
<meta charset="utf-8">
<title>Suspended Swing Stage Rentals Flyer</title>
<link rel="stylesheet" href="https://fonts.googleapis.com/css2?family=Montserrat:ital,wght@0,400;0,500;0,700;0,800;1,900&family=Saira:wght@500&display=swap">
<style>
  :root {
    --maroon: #5a0619;
    --ink: #1c1c1c;
    --paper: #ffffff;
    --backdrop: #e5e5e5;
    --soft-gray: #f1f1f1;
  }
  * { margin: 0; padding: 0; box-sizing: border-box; }
  html, body {
    width: 1183px; height: 1200px; overflow: hidden;
    background: var(--backdrop);
  }
  .flyer {
    position: absolute; left: 128px; top: 0;
    width: 927px; height: 1200px;
    background: var(--paper);
    overflow: hidden;
    font-family: "Montserrat", sans-serif;
    color: var(--ink);
  }
  .artwork { position: absolute; inset: 0; }
  .brand {
    position: absolute; left: 69px; top: 110px;
    font-family: "Montserrat", sans-serif;
    font-weight: 800; font-size: 38px; line-height: 1.05;
    color: var(--maroon); letter-spacing: 0.5px;
  }
  .services-band {
    position: absolute; left: 0; top: 269px;
    width: 327px; height: 58px;
    background: var(--maroon);
    clip-path: polygon(0 0, 100% 0, 94% 100%, 0 100%);
    border-radius: 0 6px 6px 0;
  }
  .services-band h2 {
    position: absolute; left: 69px; top: 13px;
    font-weight: 800; font-size: 25px; letter-spacing: -0.5px;
    color: var(--paper);
  }
  .services-list {
    position: absolute; left: 69px; top: 342px;
    list-style: none;
    font-family: "Saira", sans-serif; font-weight: 500;
    font-size: 17.5px; letter-spacing: 1.6px; line-height: 21px;
    color: var(--ink);
  }
  .services-list li {
    position: relative; padding-left: 25px; margin-bottom: 2.5px;
  }
  .services-list li::before {
    content: ""; position: absolute; left: 1px; top: 5px;
    width: 11px; height: 12px; background: var(--maroon);
    clip-path: polygon(0 10%, 55% 0, 100% 50%, 55% 100%, 0 90%);
    border-radius: 2px;
  }
  .headline {
    position: absolute; left: 67px; top: 636px;
    font-weight: 900; font-style: italic;
    font-size: 62px; line-height: 63px; letter-spacing: -2px;
    color: var(--maroon);
  }
  .accent-bar {
    position: absolute; left: 69px; top: 858px;
    width: 18px; height: 40px; background: var(--maroon);
  }
  .intro {
    position: absolute; left: 106px; top: 852px;
    width: 318px;
    font-weight: 500; font-size: 14.8px; line-height: 16.3px;
    color: var(--ink);
  }
  .contact-label {
    position: absolute; left: 108px; top: 1072px;
    font-weight: 500; font-size: 16.5px; color: var(--maroon);
  }
  .phone {
    position: absolute; left: 108px; top: 1093px;
    display: flex; align-items: center; gap: 10px;
    font-weight: 800; font-size: 35px; letter-spacing: -0.5px;
    color: var(--maroon);
  }
  .phone svg { width: 28px; height: 28px; }
  .website {
    position: absolute; left: 168px; top: 1136px;
    font-weight: 800; font-size: 9.5px; letter-spacing: 2.2px;
    color: var(--maroon);
  }
</style>
</head>
<body>
<main class="flyer">
  <svg class="artwork" viewBox="0 0 927 1200" width="927" height="1200">
    <defs>
      <linearGradient id="facade-tone" x1="0" y1="0" x2="1" y2="1">
        <stop offset="0" stop-color="#5b6fb8"/>
        <stop offset="0.5" stop-color="#545c9c"/>
        <stop offset="1" stop-color="#4d5a94"/>
      </linearGradient>
      <linearGradient id="street-tone" x1="0" y1="0" x2="0" y2="1">
        <stop offset="0" stop-color="#4c6a88"/>
        <stop offset="0.5" stop-color="#8c9aa6"/>
        <stop offset="1" stop-color="#b9bec4"/>
      </linearGradient>
      <linearGradient id="tower-tone" x1="0" y1="0" x2="1" y2="0">
        <stop offset="0" stop-color="#c6cbd0"/>
        <stop offset="0.35" stop-color="#3e4146"/>
        <stop offset="0.75" stop-color="#4a4d52"/>
        <stop offset="1" stop-color="#d7e1ea"/>
      </linearGradient>
    </defs>

    <path class="feature-shape" fill="#5a0619"
          d="M564 0 H927 V573 H432 Q392 573 392 533 Q392 520 402 495 Z"/>
    <path class="soft-shape" fill="#f1f1f1"
          d="M583 573 H927 V649 H623 Q583 649 583 611 Z"/>

    <path role="img" aria-label="Photo: workers on a suspended swing stage against a blue glass high-rise facade"
          fill="url(#facade-tone)"
          d="M480 82 Q488 80 500 80 H690 Q708 82 702 98 L580 490 Q576 505 560 505 H352 Q336 503 341 488 Z"/>
    <path role="img" aria-label="Photo: second view of the swing stage platform on the facade"
          fill="url(#facade-tone)"
          d="M749 96 Q754 82 770 82 H927 V240 L863 488 Q858 505 842 505 H628 Q610 504 615 488 Z"/>

    <path role="img" aria-label="Photo: crew boarding a swing stage above a city street"
          fill="url(#street-tone)"
          d="M545 803 Q550 788 567 788 H688 Q708 789 702 805 L617 1076 Q612 1090 596 1090 H452 Q432 1089 437 1072 Z"/>
    <path role="img" aria-label="Photo: swing stage hanging from a dark high-rise tower"
          fill="url(#tower-tone)"
          d="M749 803 Q754 788 771 788 H892 Q912 789 906 805 L824 1076 Q819 1090 803 1090 H656 Q636 1089 641 1072 Z"/>
  </svg>

  <div class="brand">Crestwick<br>Rentals</div>

  <div class="services-band"><h2>OUR SERVICES</h2></div>
  <ul class="services-list">
    <li>SUSPENDED SWING</li>
    <li>RIGGING SOLUTIONS</li>
    <li>COUNTER WEIGHTED<br>OUTRIGGER SYSTEM</li>
    <li>SETUP</li>
    <li>TEARDOWN</li>
    <li>OPERATION</li>
  </ul>

  <h1 class="headline">SUSPENDED<br>SWING STAGE<br>RENTALS</h1>

  <span class="accent-bar"></span>
  <p class="intro">When your team needs to work on a high-rise building and requires a safe way to access it from the outside, Crestwick Rentals Scaffolding Services has you covered. We offer suspended swing stage rentals that are easy to use and can be set up quickly. Our experts can design swing stage solutions for buildings of all shapes and sizes, making it easier for you to get the job done safely and efficiently.</p>

  <p class="contact-label">Contact us today @</p>
  <p class="phone">
    <svg viewBox="0 0 24 24" aria-hidden="true">
      <path fill="#5a0619" d="M6.6 10.8a15.2 15.2 0 0 0 6.6 6.6l2.2-2.2a1 1 0 0 1 1-.25 11.4 11.4 0 0 0 3.6.57 1 1 0 0 1 1 1V20a1 1 0 0 1-1 1A17 17 0 0 1 3 4a1 1 0 0 1 1-1h3.5a1 1 0 0 1 1 1c0 1.25.2 2.450.57 3.57a1 1 0 0 1-.25 1z"/>
      <path fill="none" stroke="#5a0619" stroke-width="1.6" stroke-linecap="round" d="M14 6.5a4 4 0 0 1 3.5 3.5M14 3a7.5 7.5 0 0 1 7 7"/>
    </svg>
    555-014-2730
  </p>
  <p class="website">WWW.CRESTWICKRENTALS.COM</p>
</main>
</body>
</html>
```